RB Cargonet businesscard project

RB Cargonet Ltd is a freshly founded small (3 employees), young (average age is 30 years) company, living from the road transportation market without own tools.
We would like to have an impressive, new-line, cool busines card for a freshly founded forwarding company on an overcrowded market which raises attention and makes the potential partners eager to work with us.

Our logo is in the attachment, please use it for the card.

Target Market(s)

The main profile of the company is logistic/forwarding on road.

Industry/Entity Type

Freight Forwarding

Contact Information for Business Card

Name: Varga Edina
Title: general manager
mobile nr: +36-70/482-5910
fax nr: +36-1/655-3947
e-mail: edina.varga@rbcargonet-example.com
info@rbcargonet-example.com
website address: http://www.rbcargonet-example.com
and if possible maybe some funny or helpful info on the back

Requirements
Must have
• contact details above
Nice to have
• some really nice and catching back-side (info, graphics, useful tool info... anything)
Should not have
• trucks, road, ship, airplane on it...

```html
<!DOCTYPE html>
<html lang="en">
<head>
<meta charset="utf-8">
<title>RB Cargonet – Business Card</title>
<link rel="stylesheet" href="https://fonts.googleapis.com/css2?family=Oswald:wght@400&family=Open+Sans:wght@400;600&display=swap">
<style>
  :root {
    --stage: #d9d9d9;
    --paper: #f3f3f1;
    --brand-blue: #7587bd;
    --line-blue: #2f7fcf;
    --icon-blue: #3a86d4;
    --ink: #2b2b2b;
    --ink-soft: #555;
  }
  * { box-sizing: border-box; margin: 0; padding: 0; }
  html, body { width: 1200px; height: 900px; overflow: hidden; }
  body {
    background: var(--stage);
    font-family: "Open Sans", sans-serif;
    color: var(--ink);
    position: relative;
  }
  .card {
    position: absolute;
    left: 340px;
    width: 520px;
    height: 300px;
    background: var(--paper);
    box-shadow: 0 6px 18px rgba(0,0,0,.12);
    overflow: hidden;
  }
  .card--front { top: 120px; }
  .card--back  { top: 480px; }

  /* shared wordmark */
  .wordmark {
    display: flex;
    align-items: center;
    gap: 14px;
  }
  .wordmark__square {
    width: 38px; height: 38px;
    background: var(--brand-blue);
  }
  .wordmark__name {
    font-family: "Oswald", sans-serif;
    font-weight: 400;
    font-size: 44px;
    color: var(--ink);
    letter-spacing: .5px;
    line-height: 1;
  }

  /* front */
  .card--front .wordmark {
    position: absolute;
    top: 88px; left: 0; right: 0;
    justify-content: center;
  }
  .front__band {
    position: absolute;
    left: 0; right: 0; bottom: 0;
    height: 72px;
    background: var(--brand-blue);
  }

  /* back */
  .card--back .wordmark {
    position: absolute;
    top: 108px; left: 38px;
  }
  .card--back .wordmark__name { font-size: 34px; }
  .card--back .wordmark__square { width: 30px; height: 30px; }
  .back__divider {
    position: absolute;
    left: 228px; top: 0;
    width: 80px; height: 300px;
  }
  .contact {
    position: absolute;
    left: 300px; top: 48px;
    width: 200px;
  }
  .contact__name {
    font-size: 18px;
    letter-spacing: .5px;
    text-transform: uppercase;
    color: var(--ink);
  }
  .contact__name strong { font-weight: 600; }
  .contact__title {
    font-size: 11px;
    color: var(--ink-soft);
    margin-top: 1px;
  }
  .contact__rule {
    border: 0;
    border-top: 1.5px solid var(--line-blue);
    margin: 14px 0 12px;
    width: 205px;
  }
  .contact__list { list-style: none; }
  .contact__item {
    display: flex;
    gap: 8px;
    align-items: flex-start;
    margin-bottom: 6px;
  }
  .contact__icon {
    flex: none;
    width: 11px; height: 11px;
    border-radius: 2px;
    background: var(--icon-blue);
    margin-top: 2px;
  }
  .contact__text {
    font-size: 9.5px;
    line-height: 1.35;
    color: var(--ink-soft);
    white-space: nowrap;
  }
</style>
</head>
<body>

  <section class="card card--front" aria-label="Business card front">
    <div class="wordmark">
      <span class="wordmark__square"></span>
      <span class="wordmark__name">RB Cargonet</span>
    </div>
    <div class="front__band"></div>
  </section>

  <section class="card card--back" aria-label="Business card back">
    <div class="wordmark">
      <span class="wordmark__square"></span>
      <span class="wordmark__name">RB Cargonet</span>
    </div>

    <svg class="back__divider" viewBox="0 0 80 300" aria-hidden="false">
      <polygon points="60,0 76,0 16,300 0,300" fill="var(--brand-blue)"/>
      <defs>
        <linearGradient id="stripeTone" x1="0" y1="0" x2="1" y2="0">
          <stop offset="0" stop-color="#9a9a9a"/>
          <stop offset="1" stop-color="#cfcfcf"/>
        </linearGradient>
      </defs>
      <polygon points="50,40 70,40 34,210 14,210" fill="url(#stripeTone)"
               role="img" aria-label="Decorative hatched texture inside the diagonal stripe"/>
    </svg>

    <div class="contact">
      <h1 class="contact__name"><strong>Varga</strong> Edina</h1>
      <p class="contact__title">general manager</p>
      <hr class="contact__rule">
      <ul class="contact__list">
        <li class="contact__item">
          <span class="contact__icon"></span>
          <span class="contact__text">mobile nr: +36-70/482-5910<br>fax nr: +36-1/655-3947</span>
        </li>
        <li class="contact__item">
          <span class="contact__icon"></span>
          <span class="contact__text">edina.varga@rbcargonet-example.com<br>info@rbcargonet-example.com</span>
        </li>
        <li class="contact__item">
          <span class="contact__icon"></span>
          <span class="contact__text">http://www.rbcargonet-example.com</span>
        </li>
      </ul>
    </div>
  </section>

</body>
</html>
```